we can communicate on this, but i want to follow the approach we took on Pell|Quorn & Tillet but i feel the card front needs the black background and the platinum and gold logo. The back? I am open. we can use the same info from PQ&T. Vellum Crest is an enhanced equity investment fund - basically a very exclusive boutique hedge fund that uses only stock options. very advanced things. hope you are interested

Contact Information for Business Card

Dr. Owen T. Brisket, CFA
Scientifique de fusée financière
555.014.2296
TheDoc4793@mailvessel.example

4718 Fennel Brook Way N.
West Fargo, ND 58078

No web site

Colors

Designer to choose colors to be used in the design.

Requirements
Nice to have
• I tend to prefer the most visible applications of the logo to include logo and name, the logo version with a black background and the gold and platinum components separated by the black. I see this working well for a single side (logo and name - this is card front to me).
• I am fairly open to other treatments on the reverse side with the data. To me, it makes sense to have a different color rendition of the logo on the reverse and it may be a muted black tone on tone or an oversized portion that would have spot UV. Or, the reverse may play with colors and layout
Should not have
• Other colors = no no
• Decorative font

```html
<!DOCTYPE html>
<html lang="en">
<head>
<meta charset="utf-8">
<title>Vellum Crest — Business Card</title>
<link href="https://fonts.googleapis.com/css2?family=Montserrat:wght@600&family=Roboto:wght@400;700&display=swap" rel="stylesheet">
<style>
  :root{
    --backdrop:#2e2e2f;
    --card:#1d1d1f;
    --card-edge:#2a2a2c;
    --emboss:#38383b;
    --gold:#d9b43a;
    --gold-deep:#b08a1c;
    --platinum:#bfbfc2;
    --ink:#f2f2f2;
  }
  *{margin:0;padding:0;box-sizing:border-box}
  html,body{width:799px;height:1200px;overflow:hidden;background:var(--backdrop)}
  .canvas{position:relative;width:799px;height:1200px}
  .card{
    position:absolute;left:100px;width:600px;height:343px;
    background:var(--card);border:1px solid var(--card-edge);
    overflow:hidden;
    box-shadow:0 14px 30px rgba(0,0,0,.45);
  }
  .card--front{top:120px}
  .card--back{top:730px}

  /* front */
  .front-mark{
    position:absolute;left:50%;top:50%;transform:translate(-50%,-50%);
    display:flex;flex-direction:column;align-items:center;gap:22px;
  }
  .front-mark__circle{width:96px;height:96px;border-radius:50%;background:var(--emboss)}
  .front-mark__name{
    font-family:'Montserrat',sans-serif;font-weight:600;white-space:nowrap;
    font-size:40px;letter-spacing:3px;color:var(--emboss);text-transform:uppercase;
  }

  /* back */
  .back-accent{position:absolute;left:-150px;top:-20px;width:383px;height:383px}
  .back-info{
    position:absolute;right:34px;top:44px;text-align:right;white-space:nowrap;
    font-family:'Roboto',sans-serif;color:var(--ink);
  }
  .brand-name{
    font-family:'Montserrat',sans-serif;font-weight:600;
    font-size:30px;letter-spacing:2px;color:var(--gold);text-transform:uppercase;
  }
  .person{margin-top:26px}
  .person__name{font-weight:700;font-size:19px;color:var(--gold)}
  .person__title{font-size:14px;margin-top:3px}
  .contact{margin-top:18px;list-style:none;font-size:14px;line-height:21px}
  .contact li{display:flex;justify-content:flex-end;align-items:center;gap:10px}
  .contact svg{width:13px;height:13px;fill:var(--gold);flex:none}
  .contact .no-icon{width:13px;flex:none}
</style>
</head>
<body>
<main class="canvas">

  <section class="card card--front" aria-label="Card front">
    <div class="front-mark">
      <div class="front-mark__circle"></div>
      <div class="front-mark__name">Vellum Crest</div>
    </div>
  </section>

  <section class="card card--back" aria-label="Card back">
    <svg class="back-accent" viewBox="0 0 383 383" aria-hidden="true">
      <defs>
        <linearGradient id="goldFill" x1="0" y1="0" x2="1" y2="1">
          <stop offset="0" stop-color="#e8c84e"/>
          <stop offset="1" stop-color="#b08a1c"/>
        </linearGradient>
      </defs>
      <circle cx="191.5" cy="191.5" r="185" fill="url(#goldFill)" stroke="#bfbfc2" stroke-width="3"/>
    </svg>

    <div class="back-info">
      <div class="brand-name">Vellum Crest</div>
      <div class="person">
        <div class="person__name">Dr. Owen T. Brisket, CFA</div>
        <div class="person__title">Scientifique de fusée financière</div>
      </div>
      <ul class="contact">
        <li>555.014.2296
          <svg viewBox="0 0 24 24"><path d="M6.6 10.8a15 15 0 0 0 6.6 6.6l2.2-2.2a1 1 0 0 1 1-.25 11.4 11.4 0 0 0 3.6.57 1 1 0 0 1 1 1V20a1 1 0 0 1-1 1A17 17 0 0 1 3 4a1 1 0 0 1 1-1h3.5a1 1 0 0 1 1 1c0 1.25.2 2.45.57 3.57a1 1 0 0 1-.25 1z"/></svg>
        </li>
        <li>TheDoc4793@mailvessel.example
          <svg viewBox="0 0 24 24"><path d="M2 5h20v14H2zm2 2v.5l8 5 8-5V7l-8 5z"/></svg>
        </li>
        <li>4718 Fennel Brook Way N.
          <svg viewBox="0 0 24 24"><path d="M12 2a7 7 0 0 0-7 7c0 5.2 7 13 7 13s7-7.8 7-13a7 7 0 0 0-7-7zm0 9.5A2.5 2.5 0 1 1 12 6.5a2.5 2.5 0 0 1 0 5z"/></svg>
        </li>
        <li>West Fargo, ND 58078<span class="no-icon"></span></li>
      </ul>
    </div>
  </section>

</main>
</body>
</html>
```